Tanning Lotion package label & Logo

Need hot new label for tanning lotion focusing on dark tanning. Sexy design must compete with soon to be dated but still popular "Pixie on the shelf" styles here:
http://www.plovermart.example/s/ref=nb_sb_noss_1?url=search-alias%3Daps&field-keywords=tanning%20lotion&sprefix=tanni%2Caps&rh=i%3Aaps%2Ck%3Atanning%20lotion
Have 30 days to complete. High end product needs right look.
Product name: SunBrimGlo
Target Market(s)
SunBrimGlo is a high-end, one-of-a-kind, multi-purpose hybrid tanning lotion that can be used indoors as a self-tanner, outdoors on the beach, or at tanning salons. The SunBrimGlo formula delivers a high performing silicone base to provide an excellent, non-irritating, non-oily, non-tacky, luxurious, light and greaseless overall feel on the skin when applied. This high performing silicon base also provides sebum absorption and control to help clear and prevent breakouts. SunBrimGlo contains a complex mixture of moisturizers and emollients including vitamin B5 to prevent and treat dry skin, protect sensitive skin, and improve skin tone and texture. It also contains a powerful blend of antioxidants including Grape Seed extract which is rich in OPC’s and has 20 times the antioxidant power of vitamin C, and 50 times the antioxidant power of vitamin E to help fight free radicals, protect and improve skin appearance and maintain healthy looking skin. SunBrimGlo contains a unique combination of two natural skin-tanning compounds to produce an even, deeper, and longer lasting tan. Tanning accelerators using natural amino acids help increase the production of melanin for a quicker and darker tan. SunBrimGlo is the most technologically advanced tanning lotion on the market today!
SunBrimGlo is a high-end product and will have a retail price point around $50 USD for 200 ml.
SunBrimGlo is aimed at the mid to high market
Target demographic are white girls and women aged 16-49, followed by white males aged 18-55.
SunBrimGlo will be sold online direct to consumers initially then followed by;
1. On shelves in beach area shops
2. In tanning salons
3. On shelves in mid-large box retail stores
Industry/Entity Type
Product
Look and feel
Each slider illustrates characteristics of the customer's brand and the style your logo design should communicate.

```html
<!DOCTYPE html>
<html lang="en">
<head>
<meta charset="utf-8">
<title>SunBrimGlo – Advanced Tanning Lotion Label</title>
<link rel="stylesheet" href="https://fonts.googleapis.com/css2?family=Bebas+Neue&family=Cinzel:wght@400;500&display=swap">
<style>
  :root {
    --backdrop-light: #f7f7f7;
    --backdrop-dark: #d9d9d9;
    --shield-black: #050505;
    --gold-light: #f8dc7a;
    --gold-mid: #d9a635;
    --gold-deep: #8a5a12;
    --gold-shadow: #4a2c06;
    --label-white: #ffffff;
    --accent-red: #c40f12;
    --outline: #111111;
  }
  html, body {
    margin: 0;
    padding: 0;
    width: 1200px;
    height: 857px;
    overflow: hidden;
  }
  body {
    background: radial-gradient(ellipse at center, var(--backdrop-light) 0%, var(--backdrop-dark) 100%);
  }
  .label-canvas {
    display: block;
    width: 1200px;
    height: 857px;
  }
  .label-kicker,
  .label-vitamins {
    font-family: "Cinzel", serif;
    fill: var(--label-white);
    text-anchor: middle;
  }
  .label-kicker { font-size: 19px; font-weight: 500; }
  .label-vitamins { font-size: 21px; }
  .label-brand {
    font-family: "Bebas Neue", sans-serif;
    font-size: 128px;
    fill: var(--label-white);
    text-anchor: middle;
  }
  .label-rank {
    font-family: "Cinzel", serif;
    font-size: 44px;
    fill: var(--accent-red);
    text-anchor: middle;
  }
  .ornament-area { fill: var(--accent-red); opacity: 0.3; }
</style>
</head>
<body>
<svg class="label-canvas" viewBox="0 0 1200 857" xmlns="http://www.w3.org/2000/svg">
  <defs>
    <linearGradient id="gold-frame" x1="0" y1="0" x2="1" y2="1">
      <stop offset="0" stop-color="var(--gold-light)"/>
      <stop offset="0.45" stop-color="var(--gold-mid)"/>
      <stop offset="0.7" stop-color="var(--gold-deep)"/>
      <stop offset="1" stop-color="var(--gold-light)"/>
    </linearGradient>
    <linearGradient id="gold-band" x1="0" y1="0" x2="1" y2="0">
      <stop offset="0" stop-color="var(--gold-deep)"/>
      <stop offset="0.25" stop-color="var(--gold-mid)"/>
      <stop offset="0.5" stop-color="var(--gold-light)"/>
      <stop offset="0.75" stop-color="var(--gold-mid)"/>
      <stop offset="1" stop-color="var(--gold-deep)"/>
    </linearGradient>
    <linearGradient id="gold-back" x1="0" y1="0" x2="0" y2="1">
      <stop offset="0" stop-color="var(--gold-mid)"/>
      <stop offset="1" stop-color="var(--gold-shadow)"/>
    </linearGradient>
  </defs>

  <g class="ribbon-back" fill="url(#gold-back)" stroke="var(--outline)" stroke-width="3">
    <path d="M345,330 Q280,300 215,270 Q260,330 250,400 Q300,370 345,400 Z"/>
    <path d="M855,330 Q920,300 985,270 Q940,330 950,400 Q900,370 855,400 Z"/>
    <path d="M330,470 Q250,450 185,480 Q215,520 150,588 Q260,560 340,560 Z"/>
    <path d="M870,470 Q950,450 1015,480 Q985,520 1050,588 Q940,560 860,560 Z"/>
  </g>

  <path class="shield-frame" fill="url(#gold-frame)" stroke="var(--outline)" stroke-width="5"
        d="M600,38 Q750,110 905,140 Q855,380 900,640 Q790,660 770,720 Q730,800 600,808 Q470,800 430,720 Q410,660 300,640 Q345,380 295,140 Q450,110 600,38 Z"/>
  <path class="shield-field" fill="var(--shield-black)"
        d="M600,75 Q740,140 865,160 Q825,380 860,620 Q760,640 740,700 Q700,770 600,775 Q500,770 460,700 Q440,640 340,620 Q375,380 335,160 Q460,140 600,75 Z"/>

  <rect class="ornament-area" x="490" y="145" width="220" height="90" rx="35"
        role="img" aria-label="Red filigree flourish ornament"/>
  <rect class="ornament-area" x="490" y="652" width="220" height="75" rx="35"
        role="img" aria-label="Red filigree flourish ornament"/>

  <text class="label-kicker" x="602" y="298">ADVANCED TANNING LOTION</text>
  <text class="label-brand" x="602" y="425" textLength="330" lengthAdjust="spacingAndGlyphs">SUNBRIMGLO</text>
  <text class="label-vitamins" x="602" y="472">WITH</text>
  <text class="label-vitamins" x="602" y="510">VITAMIN B, C &amp; E</text>

  <g class="ribbon-front" stroke="var(--outline)" stroke-width="3">
    <path fill="url(#gold-band)" d="M345,320 Q390,300 380,360 Q370,420 330,440 L330,520 Q300,470 310,400 Q315,340 345,320 Z"/>
    <path fill="url(#gold-band)" d="M855,320 Q810,300 820,360 Q830,420 870,440 L870,520 Q900,470 890,400 Q885,340 855,320 Z"/>
    <path fill="url(#gold-band)" d="M330,440 Q600,650 870,440 L870,520 Q600,750 330,520 Z"/>
  </g>
  <text class="label-rank" x="600" y="606">NO. 1</text>
</svg>
</body>
</html>
```